Packaging design for high end, natural skin care line needed

Marisa Holloway Beauty needs a label design. It is a new skin care line I am launching.
For years my line Pure Meadow Beauty was quite popular and featured in several magazines, but for personal reasons had to be shut down. Now I am launching a new line featuring PMB's top selling products, but focused solely on skin care more so than cosmetics. All products will still be handmade, but the line should still look professional-something worthy of a Fresh Larder shelf!
I am branding it with my name, as I am often quoted in articles related to gluten in beauty products, so Marisa Holloway and beauty are key words.
The key products will be facial and body serums which are packaged in .5oz., 1oz. and larger amber glass bottles with black dropper tops, I will include pictures below. For dimensions, the labels can be any size that you think will work best, but need to at the least fit the 1oz. bottle, dimensions shown here http://www.brightvialshop.example/amber-glass-round-vial/p/QX7T-52/
I loved the former PMB logo, but for Marisa Holloway Beauty I am looking for something more personal, more apothecary-like, and probably less colorful.
The line will be small, just a handful of products, but luxe, rich.
I am attaching photos of Pure Meadow Beauty's packaging for your reference.
Thanks much!!
Updates

Hi Everyone! Thank you for your submissions! Please see the links I provided in the brief, I really am looking for something more technical looking, like an apothecary. And want black text on a white background, not a black background, and nothing flowery.
Thank you all!!
Marisa

Target Market(s)

My clients are primarily women of all ages, but with more of a skin care focus, and no longer a cosmetic one, I would also like to appeal to a male audience. My clients are health conscious, gluten-free, natural, paleo, or vegan, etc. Target age is probably 25-55. Products are a bit high end, priced $45-65.

Industry/Entity Type

Cosmetics

Requirements
Must have
• It must at least say Marisa Holloway, or can say Marisa Holloway Beauty, but "Beauty" is not necessary. And capitalization is open, try whatever you think serves the brand. Likely slogans or taglines that can be included but are not essential: Care for your skin. Love and care for your skin. Handmade with love in the USA. Handmade in the USA. Think modern day apothecary. Small batch scotch. Something fine, but custom, handmade.
Nice to have
• I like the aesthetic of Tolmi Skin Care a bit http://www.rosalindtarvey.example.au/
And of Dorian Pelku as shown here http://www.pinboardly.example/pin/584203917660218447/
Also of something like this that is even customizable http://www.pinboardly.example/pin/76920418835102734/
Every product is handmade in small batches, with fine ingredients, a moderate price point of around $45-$65. And I will likely begin making custom orders. So there could be a space to say when it was made, or for whom. I would like to keep the colors classic though, I probably want to stay away from the bright pink on this one.
Should not have
• As I mentioned, probably want to stay away from a lot of color. I like black vs. gray for the text, as it will show up better in editorials. I must look good, but also photograph well. Thanks!

```html
<!DOCTYPE html>
<html lang="en">
<head>
<meta charset="utf-8">
<title>Balancing Facial Serum Label – Marisa Holloway</title>
<link href="https://fonts.googleapis.com/css2?family=Libre+Caslon+Text:wght@400&family=Open+Sans:wght@400;600&display=swap" rel="stylesheet">
<style>
  :root {
    --backdrop: #e9e9e9;
    --label-paper: #ffffff;
    --ink: #141414;
    --ink-soft: #2a2a2a;
    --edge: #d6d6d6;
  }
  * { margin: 0; padding: 0; box-sizing: border-box; }
  html, body {
    width: 1200px;
    height: 851px;
    overflow: hidden;
  }
  body {
    background: var(--backdrop);
    font-family: "Open Sans", Arial, sans-serif;
    color: var(--ink);
    display: flex;
    align-items: center;
    justify-content: center;
  }
  .label {
    width: 400px;
    height: 620px;
    background: var(--label-paper);
    border: 1px solid var(--edge);
    display: flex;
    flex-direction: column;
    align-items: center;
    padding: 40px 30px 30px;
  }
  .brand-mark {
    width: 290px;
    height: 290px;
    display: flex;
    flex-direction: column;
    align-items: center;
    justify-content: center;
    gap: 20px;
  }
  .brand-mark__ring {
    width: 150px;
    height: 150px;
    border-radius: 50%;
    border: 3px solid var(--ink);
  }
  .brand-mark__name {
    font-family: "Libre Caslon Text", Georgia, serif;
    font-size: 21px;
    font-weight: 400;
    letter-spacing: 1px;
    color: var(--ink);
  }
  .product-name {
    margin-top: 30px;
    font-size: 24px;
    font-weight: 600;
    line-height: 1.3;
    letter-spacing: 1px;
    text-align: center;
    text-transform: uppercase;
    color: var(--ink-soft);
  }
  .maker-by {
    margin-top: 18px;
    font-size: 15px;
    color: var(--ink-soft);
  }
  .maker {
    margin-top: 24px;
    width: 262px;
    border-top: 1.5px solid var(--ink);
    border-bottom: 1.5px solid var(--ink);
    padding: 5px 0 4px;
    text-align: center;
  }
  .maker__name {
    font-family: "Libre Caslon Text", Georgia, serif;
    font-size: 19px;
    font-weight: 400;
    letter-spacing: 2.5px;
    text-transform: uppercase;
    color: var(--ink);
    white-space: nowrap;
  }
  .volume {
    margin-top: auto;
    font-size: 17px;
    color: var(--ink-soft);
  }
</style>
</head>
<body>
  <main class="label">
    <div class="brand-mark">
      <span class="brand-mark__ring"></span>
      <span class="brand-mark__name">Marisa Holloway Beauty</span>
    </div>
    <h1 class="product-name">Balancing Facial<br>Serum</h1>
    <p class="maker-by">by</p>
    <div class="maker">
      <p class="maker__name">Marisa Holloway</p>
    </div>
    <p class="volume">30mL</p>
  </main>
</body>
</html>
```